Brochure Design for Velmora Shoes- Online Shoe Retailer

Specialises in ladies shoes in larger sizes. Provides excellent customer service and a great range of shoes etc. Wide range.

```html
<!DOCTYPE html>
<html lang="en">
<head>
<meta charset="utf-8">
<title>Velmora Shoes – Brochure</title>
<link rel="stylesheet" href="https://fonts.googleapis.com/css2?family=Didact+Gothic&family=Arimo:wght@400;700&display=swap">
<style>
  :root {
    --ink: #111111;
    --bar: #0c0c0c;
    --white: #ffffff;
    --coral: #f2845f;
    --coral-deep: #ef7a52;
    --hero-top: #f1eeee;
    --hero-bottom: #e6e0df;
    --paper: #fcfaf7;
    --frame: #a9a6a4;
    --photo-light: #ede8e5;
    --photo-dark: #dcd5d1;
  }
  * { box-sizing: border-box; margin: 0; padding: 0; }
  html, body { width: 1200px; height: 848px; overflow: hidden; background: var(--paper); }
  .brochure {
    position: relative; width: 1200px; height: 848px; overflow: hidden;
    font-family: "Didact Gothic", "Century Gothic", sans-serif; color: var(--ink);
    background: var(--paper);
  }

  /* top contact bar */
  .contact-bar {
    position: absolute; left: 0; top: 0; width: 1200px; height: 50px;
    background: var(--bar); color: var(--white);
    display: flex; align-items: center; justify-content: center;
    font-size: 21px; letter-spacing: 0.2px; gap: 12px;
  }
  .contact-bar .orders { color: var(--coral); text-decoration: underline; text-underline-offset: 3px; margin-right: 4px; }
  .contact-bar .divider { margin: 0 4px; }

  /* hero */
  .hero {
    position: absolute; left: 0; top: 50px; width: 1200px; height: 484px;
    background: linear-gradient(180deg, var(--hero-top), var(--hero-bottom));
  }
  .hero-photo {
    position: absolute; left: 0; top: 0; width: 500px; height: 484px;
    background: linear-gradient(160deg, var(--photo-light), var(--photo-dark));
  }
  .headline {
    position: absolute; right: 52px; top: 140px;
    font-size: 64px; font-weight: 400; letter-spacing: 0.5px; line-height: 1;
  }
  .tagline {
    position: absolute; right: 53px; top: 210px;
    font-size: 31px; color: var(--coral); line-height: 1;
  }
  .brand-name {
    position: absolute; right: 52px; top: 352px;
    display: flex; align-items: center; gap: 14px;
    font-size: 46px; color: var(--ink); line-height: 1;
  }
  .brand-name .mark { width: 26px; height: 26px; background: var(--coral); }

  /* announcement band */
  .news-band {
    position: absolute; left: 0; top: 534px; width: 1200px; height: 50px;
    background: var(--bar); color: var(--coral);
    display: flex; align-items: center; justify-content: center;
    font-size: 31px; white-space: nowrap;
  }
  .news-band .divider { margin: 0 22px 0 14px; }

  /* product row */
  .product {
    position: absolute; top: 612px; width: 170px; text-align: center;
  }
  .product-photo {
    width: 120px; height: 126px; margin: 14px auto 0; border-radius: 8px;
    background: linear-gradient(160deg, var(--tone-a), var(--tone-b));
  }
  .product-name { margin-top: 12px; font-size: 17px; color: var(--coral); }
  .price-badge { position: absolute; left: 2px; top: 0; width: 66px; height: 66px; }
  .price-badge text { font-family: "Didact Gothic", sans-serif; font-size: 17px; fill: var(--white); font-style: italic; }

  /* promo box */
  .promo {
    position: absolute; left: 963px; top: 607px; width: 194px; height: 217px;
    border: 4px solid var(--frame); background: var(--coral-deep); color: var(--white);
    font-family: "Arimo", Arial, sans-serif; font-weight: 700;
    padding: 7px 8px 0 10px; line-height: 1;
  }
  .promo .get { font-size: 25px; line-height: 1; }
  .promo .amount { font-size: 74px; letter-spacing: -2px; line-height: 0.86; margin-top: 2px; }
  .promo .off { font-size: 25px; line-height: 1; text-align: right; margin-top: 2px; }
  .promo .details { font-size: 14px; text-align: center; margin: 6px -4px 0 -6px; line-height: 1.25; }
  .promo .code { font-size: 22px; line-height: 1; display: block; }

  /* footer line */
  .visit {
    position: absolute; left: 60px; top: 806px; font-size: 25px; white-space: nowrap;
  }
  .visit .web { color: var(--coral); }
</style>
</head>
<body>
<div class="brochure">

  <header class="contact-bar">
    <span class="orders">ORDERS WELCOME</span>
    <span>Phone : 07 5550 2816</span>
    <span class="divider">|</span>
    <span>Email : sales@velmorashoes.com.au</span>
  </header>

  <section class="hero">
    <div class="hero-photo" role="img" aria-label="Photo of legs wearing white and black ruffled platform ankle boots with wooden stiletto heels"></div>
    <h1 class="headline">Stylish and fashionable</h1>
    <p class="tagline">its no longer about size</p>
    <div class="brand-name"><span class="mark"></span><span>Velmora Shoes</span></div>
  </section>

  <div class="news-band">
    <span>Ladies Shoes sizes 9-15 New Stock Available.</span>
    <span class="divider">|</span>
    <span>Winter Range now online</span>
  </div>

  <section class="products">
    <article class="product" style="left:8px; --tone-a:#a0552a; --tone-b:#5e2e14;">
      <svg class="price-badge" viewBox="0 0 66 66" aria-hidden="true"><polygon fill="var(--coral-deep)" points="33,0 39,12 52,6 50,20 64,22 55,33 64,44 50,46 52,60 39,54 33,66 27,54 14,60 16,46 2,44 11,33 2,22 16,20 14,6 27,12"/><text x="33" y="39" text-anchor="middle">$190</text></svg>
      <div class="product-photo" role="img" aria-label="Tall tan leather riding boots"></div>
      <p class="product-name">Shoe Name</p>
    </article>
    <article class="product" style="left:185px; --tone-a:#d7a66a; --tone-b:#a06c36;">
      <svg class="price-badge" viewBox="0 0 66 66" aria-hidden="true"><polygon fill="var(--coral-deep)" points="33,0 39,12 52,6 50,20 64,22 55,33 64,44 50,46 52,60 39,54 33,66 27,54 14,60 16,46 2,44 11,33 2,22 16,20 14,6 27,12"/><text x="33" y="39" text-anchor="middle">$190</text></svg>
      <div class="product-photo" role="img" aria-label="Chestnut sheepskin winter boots with buttons"></div>
      <p class="product-name">Shoe Name</p>
    </article>
    <article class="product" style="left:360px; --tone-a:#d8c7a6; --tone-b:#b56b4e;">
      <svg class="price-badge" viewBox="0 0 66 66" aria-hidden="true"><polygon fill="var(--coral-deep)" points="33,0 39,12 52,6 50,20 64,22 55,33 64,44 50,46 52,60 39,54 33,66 27,54 14,60 16,46 2,44 11,33 2,22 16,20 14,6 27,12"/><text x="33" y="39" text-anchor="middle">$190</text></svg>
      <div class="product-photo" role="img" aria-label="Striped wedge sandal"></div>
      <p class="product-name">Shoe Name</p>
    </article>
    <article class="product" style="left:545px; --tone-a:#e4ddcc; --tone-b:#a79c86;">
      <svg class="price-badge" viewBox="0 0 66 66" aria-hidden="true"><polygon fill="var(--coral-deep)" points="33,0 39,12 52,6 50,20 64,22 55,33 64,44 50,46 52,60 39,54 33,66 27,54 14,60 16,46 2,44 11,33 2,22 16,20 14,6 27,12"/><text x="33" y="39" text-anchor="middle">$190</text></svg>
      <div class="product-photo" role="img" aria-label="Woven cream flat shoes with strap"></div>
      <p class="product-name">Shoe Name</p>
    </article>
    <article class="product" style="left:727px; --tone-a:#4a4d52; --tone-b:#1f2124;">
      <svg class="price-badge" viewBox="0 0 66 66" aria-hidden="true"><polygon fill="var(--coral-deep)" points="33,0 39,12 52,6 50,20 64,22 55,33 64,44 50,46 52,60 39,54 33,66 27,54 14,60 16,46 2,44 11,33 2,22 16,20 14,6 27,12"/><text x="33" y="39" text-anchor="middle">$190</text></svg>
      <div class="product-photo" role="img" aria-label="Black studded thong sandals"></div>
      <p class="product-name">Shoe Name</p>
    </article>
  </section>

  <aside class="promo">
    <div class="get">GET</div>
    <div class="amount">10%</div>
    <div class="off">OFF</div>
    <div class="details">
      ON YOUR NEXT ORDER<br>
      SIMPLY ENTER CODE
      <span class="code">SAVEME10%</span>
      DURING CHECKOUT.
    </div>
  </aside>

  <p class="visit">Visit us online today at <span class="web">www.velmorashoes.com.au</span> to see our full range</p>

</div>
</body>
</html>
```